Business Card Re-Design for a Lighting Designer

I would like my business card re-designed. It is currently high gloss and they scratch too easily. I don not think the current design lends itself well to a matte finish. I have included the current design for reference along with our company logo.
Check out our website for current branding.
http://www.brambleorchidstudio.example

Updates
Some of the top contenders are muslim and it is a holiday for them. I do not want to discriminate and would expect the same courtesy for holidays we celebrate.
Target Market(s)
Interior Designers, Architects
Contact Information for Business Card
Logo - Name, Title, Address, Telephone Number and Extension, Email
Font styles to use
Requirements
Must have
- All the information listed on the current business card. If you use Red, it needs to be the red from our logo.
Nice to have
- Vertical and Horizontal Designs will be entertained.
Should not have
- Requirements for a glossy finish...should not look too corporate since we are a design firm.

```html
<!DOCTYPE html>
<html lang="en">
<head>
<meta charset="utf-8">
<title>Bramble Orchid Studio — Business Card</title>
<link rel="stylesheet" href="https://fonts.googleapis.com/css2?family=Roboto+Condensed:wght@300;400;700&family=Roboto:wght@400&display=swap">
<style>
  :root {
    --brand-red: #95141a;
    --ink: #1e1e1e;
    --muted-grey: #8e8e8e;
    --panel-grey: #9a9a9a;
    --paper: #ffffff;
    --backdrop: #e6e6e6;
  }
  * { box-sizing: border-box; margin: 0; padding: 0; }
  html, body { width: 1200px; height: 863px; overflow: hidden; }
  body {
    background: var(--backdrop);
    font-family: "Roboto", Arial, sans-serif;
    color: var(--ink);
  }
  .card {
    position: absolute;
    top: 169px;
    width: 300px;
    height: 525px;
    background: var(--paper);
    box-shadow: 0 2px 10px rgba(0,0,0,0.12);
    overflow: hidden;
  }
  .card--front { left: 270px; }
  .card--back { left: 630px; }

  /* Front */
  .front-header {
    position: absolute;
    left: 0; right: 0; top: 16px;
    height: 230px;
    background: var(--brand-red);
    color: var(--paper);
    padding: 56px 30px 0 30px;
  }
  .front-header__notch {
    position: absolute;
    top: -1px; left: 56px;
    width: 26px; height: 13px;
  }
  .person-name {
    font-family: "Roboto Condensed", Arial, sans-serif;
    font-weight: 700;
    font-size: 40px;
    line-height: 40px;
    text-transform: uppercase;
    padding-left: 12px;
  }
  .person-title {
    margin-top: 20px;
    border-top: 1.5px solid rgba(255,255,255,0.85);
    padding-top: 12px;
    padding-left: 12px;
    font-family: "Roboto Condensed", Arial, sans-serif;
    font-weight: 700;
    font-size: 14px;
    letter-spacing: 3.5px;
    text-transform: uppercase;
  }
  .contact {
    position: absolute;
    left: 42px; right: 24px; top: 282px;
    font-size: 13.5px;
    line-height: 19px;
  }
  .contact__group { padding: 7px 0; }
  .contact__rule { border: 0; border-top: 1.5px solid var(--brand-red); }

  /* Back */
  .brand-lockup {
    position: absolute;
    left: 34px; right: 24px; top: 60px;
  }
  .brand-lockup__mark {
    width: 56px; height: 56px;
    background: var(--brand-red);
    margin-bottom: 26px;
  }
  .brand-lockup__name {
    font-family: "Roboto Condensed", Arial, sans-serif;
    font-weight: 300;
    font-size: 40px;
    line-height: 40px;
    color: var(--ink);
    text-transform: uppercase;
  }
  .brand-rule {
    position: absolute;
    left: 34px; right: 24px; top: 310px;
    border: 0; border-top: 2px solid var(--brand-red);
  }
  .back-panel {
    position: absolute;
    left: 34px; right: 24px; top: 330px;
    height: 118px;
    background: var(--panel-grey);
  }
  .tagline {
    position: absolute;
    left: 34px; right: 24px; top: 472px;
    font-family: "Roboto Condensed", Arial, sans-serif;
    font-weight: 700;
    font-size: 15.5px;
    color: var(--muted-grey);
    text-transform: uppercase;
    letter-spacing: 0.3px;
  }
</style>
</head>
<body>
  <section class="card card--front" aria-label="Business card front">
    <div class="front-header">
      <svg class="front-header__notch" viewBox="0 0 26 13" aria-hidden="true">
        <polygon points="0,0 26,0 13,13" fill="#ffffff"/>
      </svg>
      <h1 class="person-name">Marlow<br>Fenby</h1>
      <p class="person-title">Principal</p>
    </div>
    <div class="contact">
      <div class="contact__group">
        555.014.2290x1<br>
        marlow@brambleorchidstudio.example
      </div>
      <hr class="contact__rule">
      <div class="contact__group">www.BrambleOrchidStudio.example</div>
      <hr class="contact__rule">
      <div class="contact__group">
        212 Larkspur Commons Way<br>
        Suite 40, Fairhaven<br>
        Oregon 97000, USA
      </div>
    </div>
  </section>

  <section class="card card--back" aria-label="Business card back">
    <div class="brand-lockup">
      <div class="brand-lockup__mark" aria-hidden="true"></div>
      <p class="brand-lockup__name">Bramble<br>Orchid<br>Studio</p>
    </div>
    <hr class="brand-rule">
    <div class="back-panel" role="img" aria-label="Grey panel reserved for a project image"></div>
    <p class="tagline">Lighting for Architecture</p>
  </section>
</body>
</html>
```